Wordpress Design for a Digital Management Consulting Business

I need a simple Wordpress Design and someone to set it up for a new boutique management consulting business called Tidewell Advisory that specialises in providing strategic advice to help grow digital businesses. It covers business strategy, marketing strategy, digital strategy, web product development, marketing campaigns, social, search, etc. From strategy to implementation.

URL is: tidewelladvisory.com.au

My professional background is here: au.examplenet.com/in/norabellweather

Competitors: other boutique digital/marketing management consulting businesses in Australia

The logos, colours and fonts are attached.

I would like the site to convey a business that is Smart/intelligent, Contemporary, Progressive, Digital, Energetic, Friendly.

The objective of the site is to educate visitors about what Tidewell Advisory does and encourage them to contact me for more information. It will be very light on content.

Target Market(s)

CEOs/Managing Directors, General Managers, Marketing Directors

Industry/Entity Type

Management Consulting

Font styles to use
Sans Serif

Colors
e34197
5c5c5c
000000

Requirements
Must have
• Site design requirements:
• Choose an appropriate Wordpress template, set it up for me and let me be able to edit it ongoing.
• It should use lots of images - these can be inspirational and not necessarily tied directly to the work
• Pink should feature, but not be the dominant colour.
• Site structure should be:
• 1. Home page - image led with horizontal navigation. Text beneath and images to describe the services.
• 2. About page - with space to write text and insert a picture of the Director
• 3. Services - with space to highlight services either as a list or graphically with text
• 4. Contact page - with space to write text and add email links, etc.
• Should have horizontal navigation
• It should have the flexibility to add another page
Nice to have
• Use the tree icon somehow in the design - consider in the background enlarged
• Use pink, grey, black from logo. Can introduce another complimentary colour if necessary.
• Can introduce another complimentary font to go with the logo font.
Should not have
• Use cliched business images and icons, eg. business suits, hand shakes, business men, business ties.

```html
<!DOCTYPE html>
<html lang="en">
<head>
<meta charset="utf-8">
<title>Tidewell Advisory</title>
<link href="https://fonts.googleapis.com/css2?family=Open+Sans:wght@300;400;600;700&display=swap" rel="stylesheet">
<style>
:root{
  --pink:#e34197;
  --grey:#5c5c5c;
  --black:#000000;
  --ink:#333333;
  --light:#f1f1f1;
  --rule:#e3e3e3;
  --white:#ffffff;
  --footer:#111111;
}
*{margin:0;padding:0;box-sizing:border-box}
html,body{width:798px;height:1200px;overflow:hidden}
body{font-family:'Open Sans',Arial,sans-serif;color:var(--grey);background:var(--white);position:relative}
.site-header{position:absolute;top:0;left:0;width:798px;height:58px;background:var(--white)}
.brand{position:absolute;left:66px;top:14px;display:flex;align-items:center;gap:8px}
.brand-dot{width:22px;height:22px;border-radius:50%;background:var(--pink)}
.brand-name{font-size:20px;font-weight:600;color:var(--pink);letter-spacing:.3px}
.main-nav{position:absolute;right:62px;top:30px;display:flex}
.main-nav a{display:block;padding:0 13px;line-height:28px;font-size:9.5px;text-transform:uppercase;color:var(--grey);text-decoration:none}
.main-nav a.current{color:var(--pink)}
.hero{position:absolute;top:58px;left:0;width:798px;height:275px;overflow:hidden;
  background:
    radial-gradient(ellipse 260px 150px at 470px 70px,rgba(232,186,178,.95),rgba(232,186,178,0) 70%),
    radial-gradient(ellipse 300px 200px at 640px 200px,rgba(120,146,182,.9),rgba(120,146,182,0) 75%),
    linear-gradient(100deg,#f7f5f4 0%,#eeeae8 35%,#d9d4d4 55%,#b7c2d2 78%,#dfe5ee 100%)}
.hero-caption{position:absolute;left:75px;top:110px;width:250px}
.hero-caption h1{font-size:26px;font-weight:400;color:var(--black);margin-bottom:6px}
.hero-caption p{font-size:11px;line-height:1.4;color:var(--ink)}
.section-title{position:absolute;left:66px;font-size:28px;font-weight:400;color:var(--black)}
.card{position:absolute;width:208px}
.card-photo{width:208px;height:96px}
.card h3{font-size:14px;font-weight:400;color:var(--pink);margin:14px 0 6px}
.card p{font-size:9px;line-height:1.45;color:var(--grey)}
.read-more{display:inline-block;margin-top:8px;font-size:9.5px;font-weight:700;color:var(--black);text-decoration:none}
.what-band{position:absolute;top:660px;left:0;width:798px;height:330px;background:var(--light)}
.feature{position:absolute;width:208px;top:80px}
.feature-photo{width:208px;height:100px;border:3px solid var(--pink)}
.feature h3{font-size:16px;font-weight:400;color:var(--black);margin:18px 0 6px;line-height:1.15}
.feature p{font-size:9px;line-height:1.45;color:var(--grey)}
.btn{display:inline-block;margin-top:10px;background:var(--pink);color:var(--white);font-size:9px;padding:4px 10px;text-decoration:none}
.site-footer{position:absolute;top:990px;left:0;width:798px;height:172px;background:var(--footer);color:#cfcfcf}
.footer-heading{position:absolute;top:12px;font-size:20px;font-weight:400;color:var(--white)}
.footer-list{position:absolute;top:50px;list-style:none}
.footer-list li{font-size:9px;line-height:15px;padding-left:10px;position:relative}
.footer-list li::before{content:"›";position:absolute;left:0;color:var(--pink)}
.contact-line{position:absolute;left:540px;font-size:9px;display:flex;align-items:center;gap:8px}
.contact-rule{position:absolute;left:540px;top:78px;width:190px;border-top:1px solid #333}
.social{position:absolute;left:540px;top:120px;display:flex;gap:8px}
.social span{width:18px;height:18px;border-radius:50%;border:1px solid #9a9a9a}
.copyright{position:absolute;top:1162px;left:0;width:798px;height:38px;background:var(--pink);color:var(--white);font-size:9px;text-align:center;line-height:38px}
</style>
</head>
<body>

<header class="site-header">
  <div class="brand"><span class="brand-dot"></span><span class="brand-name">Tidewell Advisory</span></div>
  <nav class="main-nav">
    <a class="current" href="#">Home</a>
    <a href="#">Services</a>
    <a href="#">About</a>
    <a href="#">Clients</a>
    <a href="#">Contact Us</a>
  </nav>
</header>

<section class="hero" role="img" aria-label="Photo of a hand touching a tablet screen">
  <div class="hero-caption">
    <h1>Tidewell Advisory</h1>
    <p>Boutique management consulting company advising digital businesses across business, product and marketing strategy.</p>
  </div>
</section>

<h2 class="section-title" style="top:368px">Our Services</h2>

<article class="card" style="left:66px;top:418px">
  <div class="card-photo" role="img" aria-label="Photo of a laptop and tablet on a desk" style="background:linear-gradient(120deg,#f4f7fb 0%,#cfdff0 40%,#6fa0d4 75%,#2f6aa8 100%)"></div>
  <h3>Digital Strategy</h3>
  <p>Lorem ipsum dolor sit amet, consectetur adipisici elit, sed eiusmod tempor incidunt ut labore et dolore magna aliqua.</p>
  <a class="read-more" href="#">Read more.</a>
</article>
<article class="card" style="left:300px;top:418px">
  <div class="card-photo" role="img" aria-label="Photo of a person working at a bright desk" style="background:linear-gradient(100deg,#8c8c8c 0%,#d6d3d0 35%,#f3f2f0 70%,#ffffff 100%)"></div>
  <h3>Marketing Strategy</h3>
  <p>Lorem ipsum dolor sit amet, consectetur adipisici elit, sed eiusmod tempor incidunt ut labore et dolore magna aliqua.</p>
  <a class="read-more" href="#">Read more.</a>
</article>
<article class="card" style="left:527px;top:418px">
  <div class="card-photo" role="img" aria-label="Photo of glowing digital network screens" style="background:radial-gradient(ellipse at 55% 45%,#8fc4f0 0%,#3a78b8 35%,#153461 70%,#0a1c38 100%)"></div>
  <h3>Digital Transformation</h3>
  <p>Lorem ipsum dolor sit amet, consectetur adipisici elit, sed eiusmod tempor incidunt ut labore et dolore magna aliqua.</p>
  <a class="read-more" href="#">Read more.</a>
</article>

<section class="what-band">
  <h2 class="section-title" style="top:28px">What we do</h2>
  <article class="feature" style="left:66px">
    <div class="feature-photo" role="img" aria-label="Photo of a team discussing ideas" style="background:linear-gradient(110deg,#e9e4de 0%,#c9a98f 40%,#6d7a8c 70%,#d9dde2 100%)"></div>
    <h3>Strategic Thinking</h3>
    <p>Lorem Ipsum has been the industry's standard dummy text ever, consectetur adipisici elit, sed eiusmod tempor.</p>
    <a class="btn" href="#">Read more</a>
  </article>
  <article class="feature" style="left:300px">
    <div class="feature-photo" role="img" aria-label="Photo of charts and reports on a table" style="background:linear-gradient(120deg,#f6f6f4 0%,#dfe6ec 40%,#9fb6c9 75%,#e9edf0 100%)"></div>
    <h3>Analytical Approach</h3>
    <p>Lorem Ipsum has been the industry's standard dummy text ever, consectetur adipisici elit, sed eiusmod tempor.</p>
    <a class="btn" href="#">Read more</a>
  </article>
  <article class="feature" style="left:527px">
    <div class="feature-photo" role="img" aria-label="Photo of colleagues in a project meeting" style="background:linear-gradient(100deg,#5f6f85 0%,#c7ab93 35%,#eae6e1 65%,#8fa3ba 100%)"></div>
    <h3>End to end project Management</h3>
    <p>Lorem Ipsum has been the industry's standard dummy text ever, consectetur.</p>
    <a class="btn" href="#">Read more</a>
  </article>
</section>

<footer class="site-footer">
  <h4 class="footer-heading" style="left:66px">Links</h4>
  <ul class="footer-list" style="left:74px">
    <li>Home</li><li>Our Services</li><li>About Us</li><li>Clients</li><li>Contact Us</li>
  </ul>
  <h4 class="footer-heading" style="left:200px">Services</h4>
  <ul class="footer-list" style="left:200px">
    <li>Business Strategy</li><li>Digital Strategy</li><li>Marketing Strategy</li><li>Product Strategy</li><li>Marketing Campaigns</li>
  </ul>
  <ul class="footer-list" style="left:366px">
    <li>Product Management</li><li>Digital Marketing</li><li>Data/CRM strategy</li><li>Content Marketing</li><li>New Product launches</li>
  </ul>
  <h4 class="footer-heading" style="left:540px">Contact Us</h4>
  <div class="contact-line" style="top:56px">
    <svg width="10" height="10" viewBox="0 0 10 10"><path d="M2 1h2l1 2.5-1.2.8a5 5 0 0 0 1.9 1.9l.8-1.2L9 6v2a1 1 0 0 1-1 1A7 7 0 0 1 1 2a1 1 0 0 1 1-1z" fill="#cfcfcf"/></svg>
    <span>Nora Bellweather &nbsp; 0412 555 018</span>
  </div>
  <div class="contact-rule"></div>
  <div class="contact-line" style="top:90px">
    <svg width="11" height="9" viewBox="0 0 11 9"><rect x=".5" y=".5" width="10" height="8" fill="none" stroke="#cfcfcf"/><path d="M.5.5l5 4 5-4" fill="none" stroke="#cfcfcf"/></svg>
    <span>nora@tidewelladvisory.com.au</span>
  </div>
  <div class="social"><span></span><span></span><span></span><span></span></div>
</footer>

<div class="copyright">© 2015 Copyright Tidewell Advisory. All Right Reserved</div>

</body>
</html>
```